Brent's Business Cards

My husband is a self employed Cabinet Maker... who contracts to Building companies and clients directly.
He installs kitchesn, designs and also completes renovations and building work.

I would like a small, FUNKY, simple but eye catching design.

It needs to incorporate the following.
Custom Cabinets / Installations / Renovations / Design

Commercial and Residential

He does not have a Website or Facebook,
contact number is 0438 207 964 and email is brentkelway@mailpost.example

I would like a Grey/Silver on black, or blue covering.. I am open to colour designs?

Thank you. :-)

Target Market(s)

Building Companies
Clients
Other Trades people onsite,. to give out at job sites

Industry/Entity Type

Business

Contact Information for Business Card

Phone: 0438 207 964
Email: brentkelway@mailpost.example

Font styles to use
Sans Serif

Colors
0592cd
747474
474747
1b1b1b
85cae6

Requirements
Must have
• Funky, simple, eye catching design
• Would like use of Silver/Grey - and a colour that would complement this.
• Am open to ideas :-)
Nice to have
• We do not have a logo or picture, will leave this up to you if you think an image would be beneficial???
• Thank you.

Files

```html
<!DOCTYPE html>
<html lang="en">
<head>
<meta charset="utf-8">
<title>Brent Kelway – Business Card</title>
<link rel="stylesheet" href="https://fonts.googleapis.com/css2?family=Exo+2:wght@400;500&family=Michroma&family=Orbitron:wght@500&display=swap">
<style>
  :root {
    --backdrop: #d6d6d6;
    --card-white: #ffffff;
    --card-black: #141414;
    --card-black-soft: #2a2a2a;
    --silver-light: #e4e4e4;
    --silver-mid: #9a9a9a;
    --silver-dark: #5e5e5e;
    --ink: #1b1b1b;
    --accent-blue: #1e3fa8;
    --contact-grey: #8a8a8a;
  }
  * { margin: 0; padding: 0; box-sizing: border-box; }
  html, body {
    width: 1200px;
    height: 900px;
    overflow: hidden;
    background: var(--backdrop);
  }
  .business-card {
    position: absolute;
    left: 100px;
    top: 165px;
    width: 1000px;
    height: 570px;
    border-radius: 42px;
    overflow: hidden;
    background: var(--card-white);
    box-shadow: 0 18px 40px rgba(0,0,0,0.25);
  }
  .card-top {
    position: absolute;
    inset: 0 0 auto 0;
    height: 300px;
    background: linear-gradient(180deg, #ffffff 0%, #f7f7f7 100%);
  }
  .brand-mark {
    position: absolute;
    left: 490px;
    top: 48px;
    width: 140px;
    height: 118px;
    border-radius: 16px;
    background: linear-gradient(180deg, #f2f2f2, #8c8c8c);
    padding: 9px;
    box-shadow: 0 6px 10px rgba(0,0,0,0.3);
  }
  .brand-mark span {
    display: block;
    width: 100%;
    height: 100%;
    border-radius: 10px;
    background: var(--accent-blue);
  }
  .owner-name {
    position: absolute;
    left: 0;
    width: 100%;
    top: 174px;
    padding-left: 120px;
    text-align: center;
    font-family: "Exo 2", sans-serif;
    font-weight: 400;
    font-size: 68px;
    color: var(--ink);
    letter-spacing: 0.5px;
  }
  .service-band {
    position: absolute;
    left: 0;
    top: 300px;
    width: 100%;
    height: 42px;
    background: linear-gradient(180deg, var(--silver-light) 0%, var(--silver-mid) 60%, var(--silver-dark) 100%);
    display: flex;
    align-items: center;
    justify-content: center;
    font-family: "Michroma", sans-serif;
    font-size: 20px;
    color: var(--ink);
    letter-spacing: 1.5px;
    white-space: nowrap;
  }
  .card-bottom {
    position: absolute;
    left: 0;
    top: 342px;
    width: 100%;
    height: 228px;
    background: radial-gradient(ellipse at 50% 40%, var(--card-black-soft) 0%, var(--card-black) 70%);
  }
  .market-line {
    position: absolute;
    top: 18px;
    left: 0;
    width: 100%;
    text-align: center;
    font-family: "Orbitron", sans-serif;
    font-weight: 500;
    font-size: 19px;
    letter-spacing: 22px;
    color: var(--accent-blue);
    text-transform: uppercase;
  }
  .contact {
    position: absolute;
    left: 0;
    width: 100%;
    padding-left: 120px;
    text-align: center;
    font-family: "Exo 2", sans-serif;
  }
  .contact-phone {
    top: 92px;
    font-size: 44px;
    font-weight: 400;
    color: var(--accent-blue);
    letter-spacing: 1px;
  }
  .contact-email {
    top: 148px;
    font-size: 30px;
    color: var(--contact-grey);
  }
</style>
</head>
<body>
  <div class="business-card">
    <div class="card-top">
      <div class="brand-mark"><span></span></div>
      <h1 class="owner-name">Brent Kelway</h1>
    </div>
    <div class="service-band">CUSTOM CABINETS / INSTALLATIONS / RENOVATIONS / DESIGN</div>
    <div class="card-bottom">
      <p class="market-line">Commercial and Residential</p>
      <p class="contact contact-phone">0438 207 964</p>
      <p class="contact contact-email">brentkelway@mailpost.example</p>
    </div>
  </div>
</body>
</html>
```